Digital Album Cover - Frosted Lanterns (Night Falls Still)

HiI need a digital album cover for a piano instrumental cover single

Artist: Corey Dalton
Title: Frosted Lanterns (Night Falls Still)

The song was originally by Derek Holloway

Please use my logo

You can listen to the track herehttps://soundcloud.com/coreydaltonkeys/frosted-lanterns-night-falls-still-piano-instrumental-cover

Requirements
Must have
• My logo design Corey Dalton

```html
<!DOCTYPE html>
<html lang="en">
<head>
<meta charset="utf-8">
<title>Frosted Lanterns (Night Falls Still) – Corey Dalton</title>
<link rel="stylesheet" href="https://fonts.googleapis.com/css2?family=Kaushan+Script&family=Montserrat:wght@400;800&display=swap">
<style>
  :root {
    --page-bg: #e9e7e4;
    --cover-black: #070606;
    --cover-dark: #1a1816;
    --cover-mid: #4a4541;
    --cover-light: #cfc9c1;
    --cover-glow: #f2eee8;
    --title-red: #e0232b;
    --ink-white: #ffffff;
  }
  * { margin: 0; padding: 0; box-sizing: border-box; }
  html, body {
    width: 1200px;
    height: 899px;
    overflow: hidden;
    background: var(--page-bg);
  }
  .album-cover {
    position: absolute;
    left: 180px;
    top: 30px;
    width: 840px;
    height: 840px;
    overflow: hidden;
    background: var(--cover-black);
    box-shadow: 0 10px 30px rgba(0,0,0,0.25);
  }
  .cover-photo {
    position: absolute;
    inset: 0;
    background:
      /* bright curve of the instrument frame, upper left */
      radial-gradient(ellipse 9% 30% at 36% 16%, rgba(242,238,232,0.75), transparent 75%),
      radial-gradient(ellipse 28% 7% at 56% 40%, rgba(207,201,193,0.45), transparent 75%),
      /* lit hand, right middle */
      radial-gradient(ellipse 26% 22% at 72% 66%, rgba(120,112,104,0.55), transparent 75%),
      /* light across the keys, lower left */
      radial-gradient(ellipse 45% 22% at 30% 86%, rgba(242,238,232,0.7), transparent 75%),
      radial-gradient(ellipse 55% 30% at 25% 78%, rgba(150,144,137,0.55), transparent 80%),
      linear-gradient(180deg, var(--cover-black) 0%, var(--cover-dark) 45%, var(--cover-mid) 75%, var(--cover-dark) 100%);
  }
  .artist-mark {
    position: absolute;
    right: 34px;
    top: 36px;
    display: flex;
    align-items: center;
    gap: 14px;
  }
  .artist-mark__dot {
    width: 80px;
    height: 80px;
    border-radius: 50%;
    background: var(--ink-white);
    flex: none;
  }
  .artist-mark__text {
    display: flex;
    flex-direction: column;
    align-items: flex-end;
  }
  .artist-mark__name {
    font-family: "Montserrat", sans-serif;
    font-weight: 800;
    font-size: 34px;
    letter-spacing: -0.5px;
    color: var(--ink-white);
    line-height: 1;
    text-transform: uppercase;
  }
  .artist-mark__tagline {
    font-family: "Montserrat", sans-serif;
    font-weight: 800;
    font-size: 14px;
    color: var(--ink-white);
    margin-top: 7px;
  }
  .title-block {
    position: absolute;
    left: 90px;
    top: 270px;
    display: flex;
    flex-direction: column;
    align-items: flex-end;
  }
  .song-title {
    font-family: "Kaushan Script", cursive;
    font-weight: 400;
    font-size: 76px;
    color: var(--title-red);
    line-height: 1.15;
    white-space: nowrap;
  }
  .song-subtitle {
    font-family: "Kaushan Script", cursive;
    font-size: 26px;
    color: var(--ink-white);
    letter-spacing: 1px;
    line-height: 1;
    text-transform: uppercase;
    white-space: nowrap;
    margin-top: -6px;
  }
</style>
</head>
<body>
  <main class="album-cover">
    <div class="cover-photo" role="img" aria-label="Close-up photograph of a hand playing piano keys in low, warm light"></div>

    <div class="artist-mark">
      <span class="artist-mark__dot"></span>
      <div class="artist-mark__text">
        <span class="artist-mark__name">Corey Dalton</span>
        <span class="artist-mark__tagline">Wedding &amp; Event Pianist</span>
      </div>
    </div>

    <div class="title-block">
      <h1 class="song-title">Frosted Lanterns</h1>
      <p class="song-subtitle">Night Falls Still</p>
    </div>
  </main>
</body>
</html>
```